Firm of surveyors needs a professional yet friendly looking flyer

Our company offers help to landlords who have a phone mast on their property. We help them to negotiate the best rent and lease terms. There are so many landlords who don't seek professional advice because they don't know it's available. We want to send them a flyer which is informative, looks professional but also friendly so it prompts them to call us. I have attached the wording and some pictures but have more I can send but they were too large to attach.

Target Market(s)

Ranges from farmers to large corporations and land owners

Industry/Entity Type

Surveyor

Font styles to use
Sans Serif

Colors
acd136
9bcb3c
000000
ffffff
606060
848484

Requirements
Must have
• Must be clear, must give a professional look, must include pictures, must include our logo, must use our colour scheme (or variations of it). Ideally, I would like a try-fold design if possible.
Nice to have
• I would like there to be stand out lines to catch the readers eye (I have included some on the wording document). I would like a clean and modern design
Should not have
• Should not be too fussy

```html
<!DOCTYPE html>
<html lang="en">
<head>
<meta charset="utf-8">
<title>The Mast Lease Co. – Tri-fold Flyer</title>
<link rel="stylesheet" href="https://fonts.googleapis.com/css2?family=Mulish:wght@400;600&family=Open+Sans:ital,wght@0,400;0,700;1,400&display=swap">
<style>
:root{
  --lime:#acd136;
  --green:#9bcb3c;
  --black:#000000;
  --white:#ffffff;
  --grey-dark:#606060;
  --grey-mid:#848484;
  --grey-cover:#575757;
  --backdrop:#e6e6e6;
  --olive:#6f7a2a;
  --sky:#3a7fd0;
}
*{box-sizing:border-box;margin:0;padding:0}
html,body{width:1200px;height:1000px;overflow:hidden}
body{background:var(--backdrop);position:relative;font-family:"Mulish",sans-serif}

/* ---------- inside spread ---------- */
.spread{position:absolute;left:30px;top:190px;width:810px;height:620px;display:flex;background:var(--black);overflow:hidden;box-shadow:0 6px 20px rgba(0,0,0,.25)}
.spread__landscape{position:absolute;left:0;right:0;bottom:0;height:380px;
  background:linear-gradient(180deg,rgba(0,0,0,0) 0%,var(--olive) 100%)}
.panel{position:relative;width:270px;height:100%;padding:28px 22px;color:var(--white);font-size:11.4px;line-height:1.48;text-align:justify}
.panel + .panel{border-left:1px solid rgba(255,255,255,.08)}
.panel p{margin-bottom:12px}
.panel__heading{font-weight:400;font-size:12.5px;letter-spacing:.4px;text-transform:uppercase;margin:0 0 10px;text-align:left}
.panel__heading--spaced{margin-top:22px}
.mast-photos{display:flex;gap:10px;margin-top:18px}
.mast-photo{width:108px;height:150px;background:var(--sky)}
.call-line{position:absolute;right:22px;bottom:44px;font-family:"Open Sans",sans-serif;font-weight:700;font-size:14px;letter-spacing:1px;color:rgba(255,255,255,.75)}

/* ---------- cover ---------- */
.cover{position:absolute;left:880px;top:190px;width:290px;height:620px;background:var(--grey-cover);overflow:hidden;font-family:"Open Sans",sans-serif;box-shadow:0 6px 20px rgba(0,0,0,.25)}
.cover__hook{position:absolute;left:24px;top:30px;right:16px;color:var(--white);line-height:1.18}
.cover__soft{color:var(--lime);font-style:italic;font-size:19px}
.cover__strong{font-weight:700;font-size:23px;text-transform:uppercase}
.cover__bands{position:absolute;left:0;top:160px;width:290px;height:340px}
.cover__photo{position:absolute;left:0;top:225px;width:290px;height:215px;background:linear-gradient(180deg,#3f7ec8 0%,#7aa6d6 100%)}
.cover__promise{position:absolute;left:20px;right:18px;top:478px;text-align:right;color:var(--white);line-height:1.2}
.cover__promise .cover__soft{font-size:15px}
.cover__promise .cover__strong{font-size:21px}
.brand-tag{position:absolute;left:58px;top:560px;width:174px;height:44px;background:var(--white);border-radius:6px;display:flex;align-items:center;justify-content:center;gap:8px}
.brand-tag__dot{width:10px;height:10px;border-radius:50%;background:var(--green)}
.brand-tag__name{font-family:"Open Sans",sans-serif;font-weight:700;font-size:14px;color:var(--grey-dark)}
</style>
</head>
<body>

<section class="spread" aria-label="Inside spread of tri-fold flyer">
  <div class="spread__landscape" role="img" aria-label="Photo of rolling green farmland with cypress trees at sunset"></div>

  <article class="panel">
    <p>Many of the original mobile phone mast leases / agreements are now coming up for renewal. This is an ideal opportunity for landlords to achieve the best deal. We are currently offering to review telecoms leases for free and provide landlords with our recommendations.</p>
    <p>Recently, operators have been attempting to cut costs by reducing rents. They are joining forces in an effort to drive rents down. Many landlords are contacting us after receiving a letter from the operators / operator's agent, telling them they must accept a rent reduction or risk losing their site. In the majority of cases, The Mast Lease Co. can prevent this from occurring and protect the landlord's rental income.</p>
    <div class="mast-photos">
      <div class="mast-photo" role="img" aria-label="Photo of a lattice telecoms mast against blue sky"></div>
      <div class="mast-photo" role="img" aria-label="Photo of a slim monopole phone mast against blue sky"></div>
    </div>
  </article>

  <article class="panel">
    <h2 class="panel__heading">Sell your phone mast</h2>
    <p>We can also assist landlords in selling their phone mast. We have strong links with many large investors who regularly purchase the freehold or leasehold interest of masts and will pay a cash lump sum of tens, even hundreds of thousands of pounds. This can be done in a matter of weeks and the cash is yours to spend however you like, regardless of whether the mast stays for the duration of the investors leasehold or not. We can negotiate flexible terms, such as a buyback option so please call us today to discuss.</p>
    <h2 class="panel__heading panel__heading--spaced">Getting a phone mast</h2>
    <p>If you don't currently have a mast located on your land but are interested in receiving thousands of pounds a year in rental income, or you have a redundant mast you would like to market, we offer a free advertising service on our website. We will market your land to phone mast operators with a view to having a mast located there. Please visit the 'Advertise My Site' link on our website to take advantage of this service.</p>
  </article>

  <article class="panel">
    <h2 class="panel__heading">The current telecoms climate</h2>
    <p>The telecoms market, in relation to mobile phone masts, is going through some huge changes. Operators are combining to cut costs. We have already seen Tri-Net join forces with Tellon and Skylink form a jointly owned company with Northwave called JTIL. More recently, Tellon and Amberline have merged to form AllReach, the new network leader. What this can mean for the landlord is changes to their site and potentially the loss of income. It can all be very confusing but don't worry, this is where we can help. We know the telecoms industry and understand how a new situation may affect a landlord, therefore, allowing us to provide the best advice on protecting your asset.</p>
    <p>In April 2017, the Government introduced the Digital Economy Act. This sets out significant changes for landlords, including the way rents are calculated. We have already seen operators contact landlords trying to reduce their rent in light of the new law. We are working alongside specialist telecoms solicitors to try to limit any potential negative impact on your income.</p>
    <div class="call-line">CALL US</div>
  </article>
</section>

<section class="cover" aria-label="Front cover">
  <div class="cover__hook">
    <div class="cover__soft">Interested in</div>
    <div class="cover__strong">Selling your site?</div>
    <div class="cover__soft">Or already have an</div>
    <div class="cover__strong">Offer?</div>
  </div>

  <div class="cover__photo" role="img" aria-label="Photo of a lattice phone mast standing on a green hillside under blue sky"></div>

  <svg class="cover__bands" viewBox="0 0 290 340" aria-hidden="true">
    <polygon points="0,20 290,40 290,70 0,66" fill="var(--lime)"/>
    <polygon points="0,50 290,20 290,66 0,66" fill="var(--green)" opacity=".85"/>
    <polygon points="0,45 120,65 0,66" fill="#6e8f22" opacity=".6"/>
    <polygon points="0,280 290,255 290,300 0,290" fill="var(--green)"/>
    <polygon points="0,268 290,300 290,310 0,300" fill="var(--lime)"/>
    <polygon points="0,300 290,310 290,340 0,340" fill="var(--grey-cover)"/>
  </svg>

  <div class="cover__promise">
    <div class="cover__soft">We can help you to achieve</div>
    <div class="cover__strong">The best sale price,</div>
    <div class="cover__soft">quickly.</div>
  </div>

  <div class="brand-tag">
    <span class="brand-tag__dot"></span>
    <span class="brand-tag__name">The Mast Lease Co.</span>
  </div>
</section>

</body>
</html>
```